Podiatry (services) Business Card

I need a business design for a New Podiatry Service.
the Podiatry services will include all aspects of podiatry including;
general podiatry for all ages
corns and callus treatment
Ingrown toenails & nail surgery
Forefoot, arch and heel pain
Gait analysis
Sports Podiatry and Orthotics
Paediatric Assessments
Diabetes Foot Assessment

I would like the back of the card to have space for next appointment day and time.

I would like a nice design that is simple yet catchy. I don't like cluttered business cards. I like things to be simple yet stand out because of the finer details.

I like the colours blue and white but I'm open to other designs that have different colours.

Kestrel Podiatry (Business name)

Leisel Marrow - Podiatrist
M.Pod.P., B.Hlth. Sci, MQFotA

Address: 58 Tolbrook Rd, Corrabel North Vic, 3168
Phone: (03) 9564 2718
Fax: (03) 9432 6581

```html
<!DOCTYPE html>
<html lang="en">
<head>
<meta charset="utf-8">
<title>Kestrel Podiatry – Business Card</title>
<link rel="stylesheet" href="https://fonts.googleapis.com/css2?family=Open+Sans:wght@400;600;700&display=swap">
<style>
  :root {
    --brand-blue: #0a78c8;
    --ink: #1c1c1c;
    --card: #ffffff;
    --backdrop: #141414;
  }
  * { box-sizing: border-box; margin: 0; padding: 0; }
  html, body { width: 1200px; height: 900px; overflow: hidden; }
  body {
    background: var(--backdrop);
    font-family: "Open Sans", Arial, sans-serif;
    position: relative;
  }
  .card {
    position: absolute;
    top: 170px;
    width: 347px;
    height: 561px;
    background: var(--card);
    text-align: center;
  }
  .card--front { left: 259px; }
  .card--back { left: 631px; }

  .band {
    position: absolute;
    left: 101px;
    width: 144px;
    height: 29px;
    background: var(--brand-blue);
  }
  .band--top { top: 0; }
  .band--bottom { bottom: 0; }

  .brand {
    position: absolute;
    top: 108px;
    left: 0;
    width: 100%;
    color: var(--brand-blue);
  }
  .brand__dot {
    display: block;
    width: 28px;
    height: 28px;
    border-radius: 50%;
    background: var(--brand-blue);
    margin: 0 auto 40px;
  }
  .brand__name {
    font-weight: 400;
    font-size: 33px;
    line-height: 38px;
    letter-spacing: 2px;
    text-transform: uppercase;
  }

  .person {
    position: absolute;
    top: 304px;
    width: 100%;
    color: var(--ink);
  }
  .person__name {
    color: var(--brand-blue);
    font-weight: 600;
    font-size: 20px;
  }
  .person__role { font-size: 15px; }
  .person__creds { font-size: 14px; margin-top: 1px; }

  .contact {
    position: absolute;
    top: 384px;
    width: 100%;
    font-size: 15px;
    color: var(--ink);
    line-height: 24px;
  }
  .contact__line {
    display: flex;
    justify-content: center;
    align-items: center;
    gap: 6px;
  }
  .contact__line svg { width: 12px; height: 12px; fill: var(--brand-blue); }

  .address {
    position: absolute;
    top: 459px;
    width: 100%;
    font-size: 15px;
    line-height: 23px;
    color: var(--ink);
  }

  .services {
    position: absolute;
    top: 103px;
    left: -5px;
    width: 100%;
    list-style: none;
    color: var(--brand-blue);
    font-weight: 600;
    font-size: 15.5px;
    line-height: 23px;
    text-transform: uppercase;
  }

  .appointment__title {
    position: absolute;
    top: 333px;
    left: -5px;
    width: 100%;
    color: var(--brand-blue);
    font-weight: 700;
    font-size: 22px;
    text-decoration: underline;
    text-underline-offset: 4px;
  }
  .appointment__field {
    position: absolute;
    left: 17px;
    right: 17px;
    display: flex;
    align-items: baseline;
    color: var(--brand-blue);
    font-weight: 600;
    font-size: 16px;
  }
  .appointment__field--name { top: 401px; }
  .appointment__field--when { top: 464px; }
  .fill {
    flex: 1;
    border-bottom: 2px dotted var(--ink);
    margin-left: 6px;
    height: 1px;
  }
  .fill--date { flex: 0 0 102px; margin-right: 4px; }
</style>
</head>
<body>
  <section class="card card--front" aria-label="Card front">
    <div class="band band--top"></div>
    <div class="brand">
      <span class="brand__dot"></span>
      <div class="brand__name">Kestrel<br>Podiatry</div>
    </div>
    <div class="person">
      <div><span class="person__name">Leisel Marrow</span> <span class="person__role">- Podiatrist</span></div>
      <div class="person__creds">M.Pod.P., B.Hlth. Sci, MQFotA</div>
    </div>
    <div class="contact">
      <div class="contact__line">
        <svg viewBox="0 0 24 24" aria-hidden="true"><path d="M6.6 10.8a15.1 15.1 0 0 0 6.6 6.6l2.2-2.2a1 1 0 0 1 1-.25 11.4 11.4 0 0 0 3.6.57 1 1 0 0 1 1 1V20a1 1 0 0 1-1 1A17 17 0 0 1 3 4a1 1 0 0 1 1-1h3.5a1 1 0 0 1 1 1c0 1.250.2 2.45.57 3.57a1 1 0 0 1-.25 1z"/></svg>
        <span>(03) 9564 2718</span>
      </div>
      <div class="contact__line">
        <svg viewBox="0 0 24 24" aria-hidden="true"><path d="M7 2h9v5H7zM4 8h16a2 2 0 0 1 2 2v10a2 2 0 0 1-2 2H4a2 2 0 0 1-2-2V10a2 2 0 0 1 2-2zm3 4v2h2v-2zm4 0v2h2v-2zm4 0v2h2v-2zm-8 4v2h2v-2zm4 0v2h2v-2zm4 0v2h2v-2z"/></svg>
        <span>(03) 9432 6581</span>
      </div>
    </div>
    <div class="address">58 Tolbrook Rd, Corrabel<br>North Vic, 3168</div>
    <div class="band band--bottom"></div>
  </section>

  <section class="card card--back" aria-label="Card back">
    <ul class="services">
      <li>General podiatry for all ages</li>
      <li>Corns and callus treatment</li>
      <li>Ingrown toenails &amp; nail surgery</li>
      <li>Forefoot, arch and heel pain</li>
      <li>Gait analysis</li>
      <li>Sports podiatry and orthotics</li>
      <li>Paediatric assessments</li>
      <li>Diabetes foot assessment</li>
    </ul>
    <div class="appointment__title">Appointment</div>
    <div class="appointment__field appointment__field--name">Name: <span class="fill"></span></div>
    <div class="appointment__field appointment__field--when">Date: <span class="fill fill--date"></span> Time: <span class="fill"></span></div>
  </section>
</body>
</html>
```